Service Plans and Offerings - One Page

We are looking for an 8.5 x 11 one page in a portrait orientation that advertises our product and service offerings on one side and our logo and a slogan, "Reliable Managed IT Services & Support" - "TALMERO is ready to earn your trust" on the other with TALMERO contact information.

This brochure would be left at prospect client's business, so it needs to be inviting, professional, and clear.

Attached is one excel sheet with 4 columns representing our Service Plans and Offerings (Ideas on the descriptive names for the different service offering level is welcome) that we would like you to use for inspiration for the written content in the handout.

The brochure should have the TALMERO contact information on the bottom of the services description page and on the other side of the page (not necessary located at bottom). TALMERO contact information (email, phone, website) will provided to contest winner.

Please be creative with both the content and the design.

Target Market(s)

Small to medium companies with 5-50 seats.

Industry/Entity Type

Information Technology (IT) Managed Service Provider

Font styles to use
Serif

Colors
0094D4
00A9DD
6FCCEA
C7EBF8
E9F6FB

Requirements
Must have
• Clear and professional representation of TALMERO Product Services Plans and easy to read TALMERO contact information.

```html
<!DOCTYPE html>
<html lang="en">
<head>
<meta charset="utf-8">
<title>TALMERO Support Plans</title>
<link href="https://fonts.googleapis.com/css2?family=Poppins:wght@300;400;500;600;700&display=swap" rel="stylesheet">
<style>
:root{
  --stage:#a9a9a9;
  --white:#ffffff;
  --ink:#1b1f29;
  --navy:#1a2233;
  --navy-deep:#0e131c;
  --blue:#1e93d2;
  --blue-bright:#00a9dd;
  --blue-soft:#5fa9dc;
  --sky:#6fccea;
  --label-bg:#e9f6fb;
  --col1:#f2f4f7;
  --col2:#eceef2;
  --col3:#dce8f0;
  --col4:#e8f1f8;
}
*{margin:0;padding:0;box-sizing:border-box}
html,body{width:1200px;height:798px;overflow:hidden}
body{background:var(--stage);font-family:"Poppins",sans-serif;color:var(--ink);position:relative}

/* ---------- plans page ---------- */
.plans-page{position:absolute;left:55px;top:54px;width:534px;height:690px;background:var(--white);overflow:hidden}
.plans-header{position:absolute;left:0;top:0;width:100%;height:45px;background:var(--navy-deep)}
.header-visual{position:absolute;left:150px;top:0;right:0;height:45px;
  background:radial-gradient(ellipse at 30% 40%,#2c3a55 0%,rgba(20,28,44,0) 60%),linear-gradient(90deg,#0f1624 0%,#1a2438 50%,#121a2a 100%)}
.header-brand-zone{position:absolute;left:0;top:0;width:150px;height:45px;background:var(--white)}
.header-brand{position:absolute;left:22px;top:12px;font-weight:600;font-size:16px;color:var(--blue);letter-spacing:.5px}
.plans-title{position:absolute;right:45px;top:8px;color:var(--white);font-weight:600;font-size:22px;line-height:1.2}
.title-rule{position:absolute;right:33px;top:19px;width:1.5px;height:14px;background:var(--blue)}

.plan-tabs{position:absolute;left:222px;top:62px;display:flex;gap:1px;z-index:2}
.plan-tab{width:69.5px;height:30px;color:var(--white);text-align:center;border-radius:0 0 10px 10px / 0 0 4px 4px;padding-top:3px;line-height:1}
.plan-tab small{display:block;font-size:8px;font-weight:500;letter-spacing:.3px}
.plan-tab b{display:block;font-size:11.5px;font-weight:600;letter-spacing:.4px}
.plan-1,.plan-4{background:var(--blue)}
.plan-2{background:var(--navy)}
.plan-3{background:var(--blue-soft)}

.plan-grid{position:absolute;left:31px;top:75px;display:grid;grid-template-columns:190px repeat(4,69.5px);column-gap:1px;grid-auto-rows:15px;row-gap:1.7px}
.group{font-weight:600;font-size:10px;padding-left:6px;line-height:15px;grid-column:1 / -1}
.feature{background:var(--label-bg);font-size:10.5px;padding-left:6px;line-height:15px;white-space:nowrap}
.cell{display:flex;align-items:center;justify-content:center}
.c1{background:var(--col1)}.c2{background:var(--col2)}.c3{background:var(--col3)}.c4{background:var(--col4)}
.tick{width:10px;height:10px}

.price-row{position:absolute;left:222px;top:612px;display:flex;gap:1px}
.price{width:69.5px;height:15.5px;color:var(--white);font-weight:600;font-size:10.5px;text-align:center;line-height:15.5px}

.plans-footer{position:absolute;left:0;bottom:0;width:100%;height:45px;background:var(--navy)}
.footer-accent{position:absolute;right:0;top:0;width:215px;height:45px;background:var(--blue);clip-path:polygon(20px 0,100% 0,100% 100%,0 100%)}
.footer-contact{position:absolute;top:0;height:45px;display:flex;align-items:center;gap:6px;color:var(--white);font-size:10.5px;font-weight:500}
.footer-contact svg{width:16px;height:16px}

/* ---------- brand page ---------- */
.brand-page{position:absolute;left:611px;top:54px;width:534px;height:690px;overflow:hidden;
  background:radial-gradient(ellipse at 50% 20%,#252c3a 0%,#161b25 55%,#0c1016 100%)}
.brand-name{position:absolute;left:0;right:0;top:150px;text-align:center;font-weight:500;font-size:40px;letter-spacing:3px;color:var(--blue)}
.brand-headline{position:absolute;left:0;right:0;top:222px;text-align:center;color:var(--white);font-weight:700;font-size:38px;line-height:46px}
.brand-slogan{position:absolute;left:0;right:0;top:318px;text-align:center;color:#e8ecf2;font-weight:300;font-size:17px}
.brand-contacts{position:absolute;left:0;right:0;top:410px}
.brand-contact{position:absolute;width:160px;margin-left:-80px;text-align:center;color:#e8ecf2;font-size:11.5px}
.brand-contact svg{display:block;margin:0 auto 9px;width:18px;height:18px}
.brand-contact::after{content:"";display:block;width:22px;height:1px;background:var(--blue);margin:13px auto 0}
.network-visual{position:absolute;left:0;right:0;bottom:0;height:185px;
  background:linear-gradient(180deg,rgba(22,27,37,0) 0%,rgba(60,68,84,.45) 50%,rgba(40,46,58,.6) 100%)}
</style>
</head>
<body>
<svg width="0" height="0" style="position:absolute">
  <defs>
    <symbol id="tk" viewBox="0 0 20 20">
      <circle cx="10" cy="10" r="9" fill="#1e93d2"/>
      <path d="M5.5 10.3l3 3 6-6.5" fill="none" stroke="#fff" stroke-width="2.2" stroke-linecap="round" stroke-linejoin="round"/>
    </symbol>
    <symbol id="ic-phone" viewBox="0 0 20 20">
      <circle cx="10" cy="10" r="9" fill="none" stroke="currentColor" stroke-width="1.2"/>
      <path d="M7 6c-.6.4-.9 1-.7 1.8.6 2.4 2.6 4.5 5 5.2.8.2 1.4-.1 1.8-.7l-1.5-1.4-1 .6c-1-.5-1.8-1.3-2.3-2.3l.6-1z" fill="none" stroke="currentColor" stroke-width="1"/>
    </symbol>
    <symbol id="ic-mail" viewBox="0 0 20 20">
      <circle cx="10" cy="10" r="9" fill="none" stroke="currentColor" stroke-width="1.2"/>
      <rect x="5.5" y="7" width="9" height="6.5" rx="1" fill="none" stroke="currentColor" stroke-width="1"/>
      <path d="M5.8 7.5L10 10.8l4.2-3.3" fill="none" stroke="currentColor" stroke-width="1"/>
    </symbol>
    <symbol id="ic-web" viewBox="0 0 20 20">
      <circle cx="10" cy="10" r="9" fill="none" stroke="currentColor" stroke-width="1.2"/>
      <circle cx="10" cy="10" r="5" fill="none" stroke="currentColor" stroke-width="1"/>
      <ellipse cx="10" cy="10" rx="2.2" ry="5" fill="none" stroke="currentColor" stroke-width="1"/>
      <path d="M5 10h10" stroke="currentColor" stroke-width="1"/>
    </symbol>
  </defs>
</svg>

<section class="plans-page">
  <header class="plans-header">
    <div class="header-visual" role="img" aria-label="Night view of the earth with city lights"></div>
    <div class="header-brand-zone"><span class="header-brand">TALMERO</span></div>
    <h1 class="plans-title">Support Plans</h1>
    <span class="title-rule"></span>
  </header>

  <div class="plan-tabs">
    <div class="plan-tab plan-1"><small>SUPPORT</small><b>PLAN 1</b></div>
    <div class="plan-tab plan-2"><small>SUPPORT</small><b>PLAN 2</b></div>
    <div class="plan-tab plan-3"><small>SUPPORT</small><b>PLAN 3</b></div>
    <div class="plan-tab plan-4"><small>SUPPORT</small><b>PLAN 4</b></div>
  </div>

  <div class="plan-grid">
    <div class="group">FORTIFY</div>
    <div class="feature">Managed Firewall</div><div class="cell c1"></div><div class="cell c2"></div><div class="cell c3"><svg class="tick"><use href="#tk"/></svg></div><div class="cell c4"><svg class="tick"><use href="#tk"/></svg></div>
    <div class="feature">AI-Based Next Gen Anti-Virus</div><div class="cell c1"></div><div class="cell c2"></div><div class="cell c3"><svg class="tick"><use href="#tk"/></svg></div><div class="cell c4"><svg class="tick"><use href="#tk"/></svg></div>
    <div class="feature">Traditional AV</div><div class="cell c1"><svg class="tick"><use href="#tk"/></svg></div><div class="cell c2"><svg class="tick"><use href="#tk"/></svg></div><div class="cell c3"></div><div class="cell c4"></div>
    <div class="feature">24/7 Security Operations Centre</div><div class="cell c1"></div><div class="cell c2"></div><div class="cell c3"><svg class="tick"><use href="#tk"/></svg></div><div class="cell c4"><svg class="tick"><use href="#tk"/></svg></div>

    <div class="group">FOUNDATION</div>
    <div class="feature">24/7 Monitoring</div><div class="cell c1"><svg class="tick"><use href="#tk"/></svg></div><div class="cell c2"><svg class="tick"><use href="#tk"/></svg></div><div class="cell c3"><svg class="tick"><use href="#tk"/></svg></div><div class="cell c4"><svg class="tick"><use href="#tk"/></svg></div>
    <div class="feature">Security Patching</div><div class="cell c1"><svg class="tick"><use href="#tk"/></svg></div><div class="cell c2"><svg class="tick"><use href="#tk"/></svg></div><div class="cell c3"><svg class="tick"><use href="#tk"/></svg></div><div class="cell c4"><svg class="tick"><use href="#tk"/></svg></div>
    <div class="feature">Application Updates</div><div class="cell c1"><svg class="tick"><use href="#tk"/></svg></div><div class="cell c2"><svg class="tick"><use href="#tk"/></svg></div><div class="cell c3"><svg class="tick"><use href="#tk"/></svg></div><div class="cell c4"><svg class="tick"><use href="#tk"/></svg></div>
    <div class="feature">Pro-active Maintenance</div><div class="cell c1"><svg class="tick"><use href="#tk"/></svg></div><div class="cell c2"><svg class="tick"><use href="#tk"/></svg></div><div class="cell c3"><svg class="tick"><use href="#tk"/></svg></div><div class="cell c4"><svg class="tick"><use href="#tk"/></svg></div>

    <div class="group">BACKUPS</div>
    <div class="feature">Offsite Backups</div><div class="cell c1"></div><div class="cell c2"></div><div class="cell c3"></div><div class="cell c4"><svg class="tick"><use href="#tk"/></svg></div>
    <div class="feature">Email Backups</div><div class="cell c1"></div><div class="cell c2"></div><div class="cell c3"></div><div class="cell c4"><svg class="tick"><use href="#tk"/></svg></div>
    <div class="feature">Onsite Backups</div><div class="cell c1"></div><div class="cell c2"><svg class="tick"><use href="#tk"/></svg></div><div class="cell c3"><svg class="tick"><use href="#tk"/></svg></div><div class="cell c4"><svg class="tick"><use href="#tk"/></svg></div>

    <div class="group">VIGILENCE</div>
    <div class="feature">Dark Web Monitoring</div><div class="cell c1"></div><div class="cell c2"></div><div class="cell c3"><svg class="tick"><use href="#tk"/></svg></div><div class="cell c4"><svg class="tick"><use href="#tk"/></svg></div>
    <div class="feature">Annual User Training</div><div class="cell c1"></div><div class="cell c2"></div><div class="cell c3"></div><div class="cell c4"><svg class="tick"><use href="#tk"/></svg></div>

    <div class="group">STRATEGY</div>
    <div class="feature">IT Strategic Planning</div><div class="cell c1"></div><div class="cell c2"></div><div class="cell c3"></div><div class="cell c4"><svg class="tick"><use href="#tk"/></svg></div>
    <div class="feature">Technology Roadmap</div><div class="cell c1"><svg class="tick"><use href="#tk"/></svg></div><div class="cell c2"><svg class="tick"><use href="#tk"/></svg></div><div class="cell c3"><svg class="tick"><use href="#tk"/></svg></div><div class="cell c4"><svg class="tick"><use href="#tk"/></svg></div>
    <div class="feature">Disaster Recovery Planning</div><div class="cell c1"></div><div class="cell c2"></div><div class="cell c3"></div><div class="cell c4"><svg class="tick"><use href="#tk"/></svg></div>

    <div class="group">REPORTS</div>
    <div class="feature">Inventory and Asset Reporting</div><div class="cell c1"></div><div class="cell c2"></div><div class="cell c3"></div><div class="cell c4"><svg class="tick"><use href="#tk"/></svg></div>
    <div class="feature">Service Delivery Reports</div><div class="cell c1"></div><div class="cell c2"></div><div class="cell c3"><svg class="tick"><use href="#tk"/></svg></div><div class="cell c4"><svg class="tick"><use href="#tk"/></svg></div>

    <div class="group">CLARITY</div>
    <div class="feature">Simplified Billing</div><div class="cell c1"><svg class="tick"><use href="#tk"/></svg></div><div class="cell c2"><svg class="tick"><use href="#tk"/></svg></div><div class="cell c3"><svg class="tick"><use href="#tk"/></svg></div><div class="cell c4"><svg class="tick"><use href="#tk"/></svg></div>
    <div class="feature">Lifecycle Planning</div><div class="cell c1"></div><div class="cell c2"></div><div class="cell c3"><svg class="tick"><use href="#tk"/></svg></div><div class="cell c4"><svg class="tick"><use href="#tk"/></svg></div>
    <div class="feature">Budgeting</div><div class="cell c1"></div><div class="cell c2"></div><div class="cell c3"><svg class="tick"><use href="#tk"/></svg></div><div class="cell c4"><svg class="tick"><use href="#tk"/></svg></div>
    <div class="feature">Vendor Liason</div><div class="cell c1"><svg class="tick"><use href="#tk"/></svg></div><div class="cell c2"><svg class="tick"><use href="#tk"/></svg></div><div class="cell c3"><svg class="tick"><use href="#tk"/></svg></div><div class="cell c4"><svg class="tick"><use href="#tk"/></svg></div>
    <div class="feature">Procurement</div><div class="cell c1"><svg class="tick"><use href="#tk"/></svg></div><div class="cell c2"><svg class="tick"><use href="#tk"/></svg></div><div class="cell c3"><svg class="tick"><use href="#tk"/></svg></div><div class="cell c4"><svg class="tick"><use href="#tk"/></svg></div>

    <div class="group">USER SUPPORT</div>
    <div class="feature">Unlimited Support</div><div class="cell c1"><svg class="tick"><use href="#tk"/></svg></div><div class="cell c2"><svg class="tick"><use href="#tk"/></svg></div><div class="cell c3"><svg class="tick"><use href="#tk"/></svg></div><div class="cell c4"><svg class="tick"><use href="#tk"/></svg></div>
  </div>

  <div class="price-row">
    <div class="price plan-1">$50.00</div>
    <div class="price plan-2">$89.00</div>
    <div class="price plan-3">$119.00</div>
    <div class="price plan-4">$145.00</div>
  </div>

  <footer class="plans-footer">
    <div class="footer-accent"></div>
    <div class="footer-contact" style="left:40px"><svg style="color:var(--sky)"><use href="#ic-phone"/></svg>+01 555 0142</div>
    <div class="footer-contact" style="left:166px"><svg style="color:var(--sky)"><use href="#ic-mail"/></svg>info@talmero.com</div>
    <div class="footer-contact" style="left:369px"><svg style="color:var(--white)"><use href="#ic-web"/></svg>www.TALMERO.com</div>
  </footer>
</section>

<section class="brand-page">
  <div class="brand-name">TALMERO</div>
  <h2 class="brand-headline">Reliable Managed IT<br>Services &amp; Support</h2>
  <p class="brand-slogan">TALMERO is ready to earn your trust</p>
  <div class="brand-contacts">
    <div class="brand-contact" style="left:126px"><svg style="color:var(--blue)"><use href="#ic-phone"/></svg>+01 555 0142</div>
    <div class="brand-contact" style="left:266px"><svg style="color:var(--blue)"><use href="#ic-mail"/></svg>info@talmero.com</div>
    <div class="brand-contact" style="left:406px"><svg style="color:var(--blue)"><use href="#ic-web"/></svg>www.TALMERO.com</div>
  </div>
  <div class="network-visual" role="img" aria-label="Faint network of connected points and lines"></div>
</section>
</body>
</html>
```